Meridel Hair Studio Needs a new appointment business card

We need a new appointment card for our hair salon.

I Dont want bright out there colours.
I would like it to be neat, clean, easy to read. White, Black, with a hint of colour if needed.

We need
-Logo
-Phone number 47208613
-Mobile Number: 0417306852
Address: Shop 3/214 Calder Road, The Elmgates, Tallowbank 4812

BACK SIDE OF CARD
- Appointment Time & Date (White background so we are able to write on it)
(If you are unable to make your appointment please contact us ASAP 47208613)

I also would like the chatterly and Pictorama logo(Find us on Chatterly)(find us on Pictorama)

Target Market(s)

appointment card simple to read. all information for their next appoint For all our clients male and female

Industry/Entity Type

Hairdresser

Contact Information for Business Card

-Logo
-Phone number 47208613

BACK SIDE OF CARD

Font styles to use
Serif
Sans Serif
Script

Requirements
Must have
• White Back ground on backside with appointment deatils so we are able to write information (like appointment time and date)
Nice to have
• Find us on Chatterly
and
pictorama - meridel_hairstudio
Should not have
• BRIGHT COLOURS

```html
<!DOCTYPE html>
<html lang="en">
<head>
<meta charset="utf-8">
<title>Meridel Hair Studio – Appointment Card</title>
<link rel="stylesheet" href="https://fonts.googleapis.com/css2?family=Rokkitt:wght@400&family=Arimo:wght@400&display=swap">
<style>
  :root {
    --canvas: #d6d7d9;
    --ink: #231f20;
    --paper: #ffffff;
    --silver-light: #e6e6e6;
    --silver-dark: #8a8a8a;
    --line: #333333;
    --serif: "Rokkitt", Georgia, serif;
    --sans: "Arimo", Arial, sans-serif;
  }
  html, body {
    margin: 0;
    width: 1200px;
    height: 1200px;
    overflow: hidden;
    background: var(--canvas);
  }
  .canvas { position: relative; width: 1200px; height: 1200px; }
  .card {
    position: absolute;
    width: 700px;
    height: 400px;
    border-radius: 22px;
    overflow: hidden;
    background: var(--paper);
    box-sizing: border-box;
    border: 1px solid var(--line);
  }
  .card svg.card-art { position: absolute; inset: 0; width: 700px; height: 400px; }
  .card--front { left: 179px; top: 189px; }
  .card--back { left: 329px; top: 610px; }

  .brand {
    position: absolute;
    left: 76px;
    top: 68px;
    color: var(--paper);
    font-family: var(--serif);
    font-weight: 400;
    display: flex;
    align-items: center;
    gap: 12px;
  }
  .brand__mark {
    width: 14px; height: 14px;
    border-radius: 50%;
    background: var(--paper);
  }
  .brand__name { font-size: 40px; letter-spacing: 2px; line-height: 1; }
  .brand__name small { display: block; font-size: 15px; letter-spacing: 3px; margin-top: 6px; }

  .contact {
    position: absolute;
    left: 382px;
    top: 258px;
    font-family: var(--serif);
    font-size: 17px;
    color: var(--ink);
    line-height: 23px;
  }
  .contact__row { display: flex; align-items: flex-start; gap: 14px; }
  .contact__row + .contact__row { margin-top: 1px; }
  .contact__row--address { margin-top: 4px; }
  .contact__icon { width: 14px; height: 14px; margin-top: 4px; flex: none; }

  .appointment {
    position: absolute;
    left: 39px;
    top: 190px;
    font-family: var(--serif);
    color: var(--ink);
  }
  .appointment__title { font-size: 19px; letter-spacing: 0; margin: 0 0 34px; font-weight: 400; line-height: 24px; }
  .appointment__field { display: flex; align-items: flex-end; font-size: 17px; height: 24px; margin-bottom: 23px; }
  .appointment__label { width: 78px; }
  .appointment__blank { width: 155px; border-bottom: 1px solid var(--ink); height: 18px; }
  .appointment__suffix { font-family: var(--sans); font-size: 11px; margin-left: 24px; margin-bottom: -2px; }

  .social {
    position: absolute;
    right: 30px;
    bottom: 36px;
    display: flex;
    gap: 22px;
    font-family: var(--serif);
    font-size: 16px;
    color: var(--paper);
  }
  .social__item { display: flex; align-items: center; gap: 8px; }
  .social__dot { width: 12px; height: 12px; border-radius: 50%; border: 1px solid var(--paper); }
</style>
</head>
<body>
<div class="canvas">

  <section class="card card--front">
    <svg class="card-art" viewBox="0 0 700 400">
      <defs>
        <linearGradient id="silverFront" x1="0" y1="0" x2="1" y2="0">
          <stop offset="0" stop-color="var(--silver-dark)"/>
          <stop offset="0.5" stop-color="var(--silver-light)"/>
          <stop offset="1" stop-color="var(--silver-dark)"/>
        </linearGradient>
      </defs>
      <polygon class="panel-dark" points="0,0 462,0 290,400 0,400" fill="var(--ink)"/>
      <polygon role="img" aria-label="Silver hairdressing scissors illustration along the split"
               points="444,0 468,0 320,400 222,400" fill="url(#silverFront)"/>
    </svg>

    <div class="brand">
      <span class="brand__name">MERIDEL<small>HAIR STUDIO</small></span>
      <span class="brand__mark"></span>
    </div>

    <div class="contact">
      <div class="contact__row">
        <svg class="contact__icon" viewBox="0 0 14 14"><path d="M3 1l2 3-1.3 1.3a8 8 0 004 4L9 8l3 2-1.2 2.5C6 12 2 8 1.5 3.2z" fill="var(--ink)"/></svg>
        <span>47208613</span>
      </div>
      <div class="contact__row">
        <svg class="contact__icon" viewBox="0 0 14 14"><rect x="3.5" y="1" width="7" height="12" rx="1.2" fill="none" stroke="var(--ink)" stroke-width="1.6"/></svg>
        <span>0417306852</span>
      </div>
      <div class="contact__row contact__row--address">
        <svg class="contact__icon" viewBox="0 0 14 14"><path d="M7 1a4.3 4.3 0 00-4.3 4.3C2.7 8.5 7 12 7 12s4.3-3.5 4.3-6.7A4.3 4.3 0 007 1z" fill="var(--ink)"/><circle cx="7" cy="5.3" r="1.6" fill="var(--paper)"/><rect x="3" y="12.2" width="8" height="1.3" fill="var(--ink)"/></svg>
        <span>Shop 3/214 Calder Road,<br>The Elmgates, Tallowbank 4812</span>
      </div>
    </div>
  </section>

  <section class="card card--back">
    <svg class="card-art" viewBox="0 0 700 400">
      <defs>
        <linearGradient id="silverBack" x1="0" y1="0" x2="1" y2="0">
          <stop offset="0" stop-color="var(--silver-dark)"/>
          <stop offset="0.5" stop-color="var(--silver-light)"/>
          <stop offset="1" stop-color="var(--silver-dark)"/>
        </linearGradient>
      </defs>
      <polygon class="panel-dark" points="250,0 700,0 700,400 470,400" fill="var(--ink)"/>
      <polygon role="img" aria-label="Silver hairdressing scissors illustration along the split"
               points="236,0 258,0 480,400 400,400" fill="url(#silverBack)"/>
    </svg>

    <div class="appointment">
      <h2 class="appointment__title">YOUR NEXT APPOINTMENT IS</h2>
      <div class="appointment__field">
        <span class="appointment__label">DATE:</span>
        <span class="appointment__blank"></span>
      </div>
      <div class="appointment__field">
        <span class="appointment__label">TIME:</span>
        <span class="appointment__blank"></span>
        <span class="appointment__suffix">AM/PM</span>
      </div>
    </div>

    <div class="social">
      <span class="social__item"><span class="social__dot"></span>Chatterly</span>
      <span class="social__item"><span class="social__dot"></span>Pictorama</span>
    </div>
  </section>

</div>
</body>
</html>
```